Letterhead for Law Firm - Logo already prepared

I previously used to prepare a logo which I was quite pleased with, a copy is attached for your reference. I would like the font of the logo to be all the same size, rather than the 'S' and 'L' being larger than the other letters.
I have copies of the attached in other formats if necessary.
I need a letterhead prepared which is virtually identical to the draft attached, however I will be adding an address, phone number, fax number, mobile number and email. I will provide these details with whoever can assist me.
I will also be providing insurance details to be listed at the foot of the page.
Finally, I need the file to be supplied as a high resolution pdf with 2mm bleed.
If you require any further information, please do not hesitate to contact me.

```html
<!DOCTYPE html>
<html lang="en">
<head>
<meta charset="utf-8">
<title>Brannock Legal – Letterhead</title>
<link rel="stylesheet" href="https://fonts.googleapis.com/css2?family=Cinzel:wght@500&family=Tinos&family=Lato&display=swap">
<style>
  :root {
    --paper-top: #ffffff;
    --paper-bottom: #efefef;
    --ink: #1f1f1f;
    --ink-soft: #444444;
    --accent: #ea5a17;
    --accent-faint: rgba(240, 120, 50, 0.07);
    --rule: #c8c8c8;
    --social: #3b5998;
  }
  * { margin: 0; padding: 0; box-sizing: border-box; }
  html, body { width: 960px; height: 1200px; overflow: hidden; background: #ffffff; }
  .letterhead {
    position: relative;
    width: 960px;
    height: 1200px;
    overflow: hidden;
    background: linear-gradient(150deg, var(--paper-top) 35%, var(--paper-bottom) 100%);
    font-family: "Tinos", "Times New Roman", serif;
    color: var(--ink-soft);
  }
  .brand {
    position: absolute;
    left: 32px;
    top: 34px;
    display: flex;
    align-items: center;
    gap: 18px;
  }
  .brand-mark {
    width: 94px;
    height: 94px;
    border-radius: 50%;
    background: var(--accent);
    flex: none;
  }
  .brand-name {
    font-family: "Cinzel", "Trajan Pro", serif;
    font-weight: 500;
    font-size: 34px;
    line-height: 1;
    letter-spacing: 1px;
    text-transform: uppercase;
    font-variant: normal;
    white-space: nowrap;
    color: var(--ink);
  }
  .address {
    position: absolute;
    left: 730px;
    top: 60px;
    padding-left: 11px;
    border-left: 1px solid var(--rule);
    font-size: 19px;
    line-height: 22px;
    font-style: normal;
    white-space: nowrap;
  }
  .backdrop {
    position: absolute;
    left: 247px;
    top: 367px;
  }
  .contacts {
    position: absolute;
    left: 20px;
    top: 1078px;
    list-style: none;
    font-size: 15.5px;
    line-height: 16.8px;
    color: var(--ink-soft);
  }
  .contacts li { display: flex; align-items: center; gap: 4px; white-space: nowrap; }
  .contacts svg { width: 11px; height: 11px; flex: none; }
  .social-box { width: 10px; height: 10px; background: var(--social); border-radius: 1px; flex: none; margin-right: 1px; }
  .insurance {
    position: absolute;
    left: 387px;
    top: 1141px;
    width: 545px;
    font-family: "Lato", "Helvetica Neue", sans-serif;
    font-size: 8.6px;
    line-height: 13px;
    color: var(--ink-soft);
    white-space: nowrap;
  }
</style>
</head>
<body>
<main class="letterhead">
  <header class="brand">
    <div class="brand-mark" aria-hidden="true"></div>
    <h1 class="brand-name">Brannock Legal</h1>
  </header>

  <address class="address">
    Street Name, City Name<br>
    State, City Zip Code
  </address>

  <svg class="backdrop" width="460" height="470" viewBox="0 0 460 470" aria-hidden="true">
    <ellipse cx="230" cy="235" rx="212" ry="225" fill="var(--accent-faint)" stroke="rgba(240,120,50,0.06)" stroke-width="24"/>
  </svg>

  <ul class="contacts">
    <li>
      <svg viewBox="0 0 12 12"><path d="M3 1l2 2.5-1.2 1.2a7 7 0 0 0 3.5 3.5L8.5 7 11 9l-1.5 2C5 11 1 7 1 2.5z" fill="var(--accent)"/></svg>
      98-5210-3377
    </li>
    <li>
      <svg viewBox="0 0 12 12"><rect x="3.5" y="1" width="5" height="10" rx="1" fill="var(--accent)"/><rect x="4.5" y="2.3" width="3" height="5" fill="#fff"/></svg>
      12-4870-2615
    </li>
    <li>
      <svg viewBox="0 0 12 12"><rect x="3" y="1.5" width="6" height="4" fill="var(--accent)"/><rect x="1" y="5" width="10" height="5.5" rx="1" fill="var(--accent)"/><rect x="3" y="7" width="6" height="1.2" fill="#fff"/></svg>
      12-4870-2615
    </li>
    <li>
      <svg viewBox="0 0 12 12"><rect x="1" y="3" width="10" height="7" rx="1" fill="var(--accent)"/><path d="M1.5 3.5L6 7l4.5-3.5" stroke="#fff" stroke-width="1" fill="none"/></svg>
      infobrannocklegal.com
    </li>
    <li>
      <svg viewBox="0 0 12 12"><circle cx="6" cy="6" r="4.8" fill="none" stroke="var(--accent)" stroke-width="1.2"/><path d="M1.5 6h9M6 1.2v9.6" stroke="var(--accent)" stroke-width="0.9"/><ellipse cx="6" cy="6" rx="2.2" ry="4.8" fill="none" stroke="var(--accent)" stroke-width="0.9"/></svg>
      www.brannocklegal.com
    </li>
    <li>
      <span class="social-box" aria-hidden="true"></span>
      /brannocklegal
    </li>
  </ul>

  <footer class="insurance">
    <p>Lorem ipsum dolor sit amet, consectetuer adipiscing elit, sed diam nonummy nibh euismod tincidunt ut laoreet Lorem ipsumLorem ipsum</p>
    <p>Lorem ipsum dolor sit amet, consectetuer adipiscing elit, sed diam nonummy nibh euismod tincidunt ut laoreet Lorem ipsumLorem ipsum</p>
    <p>Lorem ipsum dolor sit amet, consectetuer adipiscing elit, sed diam nonummy nibh euismod tincidunt ut laoreet Lorem ipsumLorem ipsum</p>
  </footer>
</main>
</body>
</html>
```